The Wardrobe Sage needs a business card

The wardrobe sage is a lead generation service serving the Custom Closet industry.

Here is the basic card information:

The Wardrobe Sage
Dorian Pettigrew
Owner/CEO
Briarwood, NC
704-318-5527 Cell
Email: dpettigrew@TheWardrobeSage.com

Additional information for the card:

"High quality, flat rate lead generation exclusively for the custom closet industry"

Bullet points for the back:

- Low fixed cost
- Easy to budget
- Guaranteed qualified Leeds
- Exclusivity per city

Logo attached, head shot attached. Photos of closet systems attached

```html
<!DOCTYPE html>
<html lang="en">
<head>
<meta charset="utf-8">
<title>The Wardrobe Sage – Business Card</title>
<link rel="stylesheet" href="https://fonts.googleapis.com/css2?family=Open+Sans:wght@400;600;700&display=swap">
<style>
  :root {
    --backdrop: #474747;
    --card: #ffffff;
    --bronze: #a8652a;
    --slate: #55565a;
    --suit-dark: #1f2a44;
    --suit-light: #5a6680;
  }
  * { box-sizing: border-box; margin: 0; padding: 0; }
  html, body {
    width: 1200px; height: 801px; overflow: hidden;
    background: var(--backdrop);
    font-family: "Open Sans", Arial, sans-serif;
  }
  .stage { position: relative; width: 1200px; height: 801px; }
  .card {
    position: absolute; top: 250px;
    width: 525px; height: 300px;
    background: var(--card);
    border-radius: 18px;
    border-bottom: 3px solid var(--bronze);
    overflow: hidden;
    box-shadow: 0 16px 30px rgba(0,0,0,.35);
  }
  .card--front { left: 50px; }
  .card--back { left: 625px; }

  /* front */
  .headshot {
    position: absolute; right: 0; top: 0;
    width: 230px; height: 300px;
    background: linear-gradient(160deg, var(--suit-light) 0%, var(--suit-dark) 60%, #141b2e 100%);
    clip-path: polygon(30% 0, 100% 0, 100% 100%, 8% 100%, 14% 40%);
  }
  .brand-name {
    position: absolute; left: 36px; top: 40px;
    display: flex; align-items: center; gap: 10px;
    font-size: 24px; font-weight: 600; color: var(--slate);
    line-height: 1;
  }
  .brand-dot { width: 12px; height: 12px; border-radius: 50%; background: var(--bronze); flex: none; }
  .accent-tab {
    position: absolute; left: 0; top: 132px;
    width: 22px; height: 40px; background: var(--bronze);
  }
  .person { position: absolute; left: 36px; top: 122px; }
  .person__name { font-size: 24px; font-weight: 700; color: var(--bronze); line-height: 1.1; }
  .person__title { font-size: 14px; color: var(--slate); margin-top: 2px; }
  .contact { position: absolute; left: 36px; top: 196px; list-style: none; }
  .contact li {
    display: flex; align-items: center; gap: 8px;
    font-size: 13px; color: var(--slate); line-height: 1.7;
  }
  .contact svg { width: 12px; height: 12px; flex: none; }

  /* back */
  .back-brand {
    position: absolute; left: 0; right: 0; top: 78px;
    display: flex; justify-content: center; align-items: center; gap: 14px;
    font-size: 44px; font-weight: 600; color: var(--slate); line-height: 1;
  }
  .back-brand .brand-dot { width: 18px; height: 18px; }
  .tagline {
    position: absolute; left: 0; right: 0; top: 166px;
    text-align: center; font-size: 13.5px; color: var(--slate);
  }
  .benefits {
    position: absolute; left: 0; right: 0; top: 198px;
    display: grid; grid-template-columns: auto auto; justify-content: center;
    column-gap: 14px; row-gap: 4px; list-style: none;
    font-size: 15px; color: var(--slate);
  }
  .benefits li:nth-child(odd) { text-align: right; }
  .benefits li:nth-child(even)::before {
    content: ""; display: inline-block; width: 9px; height: 9px;
    border-radius: 50%; background: var(--bronze); margin-right: 8px;
  }
</style>
</head>
<body>
<main class="stage">
  <section class="card card--front" aria-label="Business card front">
    <div class="headshot" role="img" aria-label="Portrait of Dorian Pettigrew in a navy plaid blazer, arms crossed"></div>
    <div class="brand-name"><span class="brand-dot"></span>The Wardrobe Sage</div>
    <div class="accent-tab"></div>
    <div class="person">
      <p class="person__name">Dorian Pettigrew</p>
      <p class="person__title">Owner/CEO</p>
    </div>
    <ul class="contact">
      <li><svg viewBox="0 0 12 12"><path d="M6 0a4 4 0 0 1 4 4c0 3-4 8-4 8S2 7 2 4a4 4 0 0 1 4-4z" fill="var(--bronze)"/><circle cx="6" cy="4" r="1.5" fill="#fff"/></svg>Briarwood, NC</li>
      <li><svg viewBox="0 0 12 12"><rect x="3" y="0.5" width="6" height="11" rx="1" fill="none" stroke="var(--bronze)" stroke-width="1.2"/></svg>704-318-5527</li>
      <li><svg viewBox="0 0 12 12"><rect x="0.5" y="2" width="11" height="8" fill="var(--bronze)"/><path d="M0.5 2l5.5 4 5.5-4" fill="none" stroke="#fff" stroke-width="1"/></svg>dpettigrew@TheWardrobeSage.com</li>
    </ul>
  </section>

  <section class="card card--back" aria-label="Business card back">
    <div class="back-brand"><span class="brand-dot"></span>The Wardrobe Sage</div>
    <p class="tagline">High quality, flat rate lead generation exclusively for the custom closet industry</p>
    <ul class="benefits">
      <li>Low fixed cost</li>
      <li>Guaranteed qualified Leeds</li>
      <li>Easy to budget</li>
      <li>Exclusivity per city</li>
    </ul>
  </section>
</main>
</body>
</html>
```